custom carpentry, woodworking and home repair company needs logo design and business card design

Attention: I apologize but I just received notification from my state that I cannot use the company name that I originally submitted (Beyond The Bench). The new name will be Lumbrella We need a company logo and business card design for our new company based in the Hampton Roads area of Virginia. The company name is Lumbrella. The final design should give a first impression of true craftsmanship and attention to detail. We would like the card to include the company name, my name Derek Halloway (owner), phone number (757) 482-3175, website (lumbrella-shop.example) and email address (derek@lumbrella-shop.example). Everything else is up to your discretion. Thanks, have fun, and good luck.

Industry/Entity Type

Business

Contact Information for Business Card

See project description

Logo Text

see project description

Colors

Designer to choose colors to be used in the design.

```html
<!DOCTYPE html>
<html lang="en">
<head>
<meta charset="utf-8">
<title>Lumbrella Business Card</title>
<link href="https://fonts.googleapis.com/css2?family=Libre+Baskerville:wght@400;700&display=swap" rel="stylesheet">
<style>
  :root {
    --ink: #222a28;
    --accent: #8a0a0a;
    --paper: #ffffff;
    --backdrop: #c4c4c4;
  }
  html, body {
    margin: 0;
    padding: 0;
    width: 1200px;
    height: 1200px;
    overflow: hidden;
    background: var(--backdrop);
    font-family: "Libre Baskerville", Georgia, serif;
    color: var(--ink);
  }
  .card {
    position: absolute;
    left: 216px;
    width: 796px;
    height: 453px;
    background: var(--paper);
  }
  .card--front { top: 136px; }
  .card--back { top: 614px; }

  .wordmark { position: absolute; overflow: visible; }
  .wordmark text {
    font-family: "Libre Baskerville", Georgia, serif;
    font-weight: 700;
    fill: var(--ink);
  }
  .card--front .wordmark { left: 368px; top: 140px; width: 360px; height: 60px; }
  .card--back .wordmark { left: 124px; top: 232px; width: 548px; height: 90px; }

  .owner-name {
    position: absolute;
    left: 71px;
    top: 222px;
    margin: 0;
    font-size: 33px;
    font-weight: 700;
    line-height: 1;
    color: #111;
  }
  .owner-role {
    position: absolute;
    left: 72px;
    top: 262px;
    margin: 0;
    font-size: 22px;
    line-height: 1;
  }
  .contact {
    position: absolute;
    top: 327px;
    display: flex;
    align-items: center;
    gap: 9px;
    font-size: 19px;
    line-height: 1;
    color: #111;
  }
  .contact--phone { left: 71px; }
  .contact--email { left: 322px; }
  .contact svg { width: 25px; height: 25px; flex: none; }

  .rule {
    position: absolute;
    left: 71px;
    top: 360px;
    width: 654px;
    height: 5px;
    border-radius: 3px;
    background: var(--accent);
  }
  .website {
    position: absolute;
    left: 0;
    width: 796px;
    text-align: center;
    margin: 0;
    line-height: 1;
    color: #111;
  }
  .card--front .website { top: 376px; font-size: 24px; letter-spacing: 2px; padding-left: 0; }
  .card--back .website { top: 348px; font-size: 21px; letter-spacing: 10px; }
</style>
</head>
<body>

<section class="card card--front">
  <svg class="wordmark" viewBox="0 0 360 60" aria-label="Lumbrella">
    <text x="360" y="50" text-anchor="end" font-size="50" textLength="356" lengthAdjust="spacingAndGlyphs">LUMBRELLA</text>
  </svg>

  <h1 class="owner-name">Derek Halloway</h1>
  <p class="owner-role">Owner</p>

  <div class="contact contact--phone">
    <svg viewBox="0 0 24 24" aria-hidden="true">
      <circle cx="12" cy="12" r="12" fill="var(--accent)"/>
      <path d="M7.5 6.5c.6-.6 1.4-.6 1.9 0l1.3 1.6c.4.5.3 1.2-.1 1.6l-.7.6c.6 1.4 1.8 2.6 3.2 3.2l.6-.7c.4-.4 1.1-.5 1.6-.1l1.6 1.3c.6.5.6 1.3 0 1.9l-1 1c-.8.8-2.2.9-3.4.3-2.4-1.2-4.4-3.2-5.6-5.6-.6-1.2-.5-2.6.3-3.4z" fill="#fff"/>
    </svg>
    <span>(757) 482-3175</span>
  </div>

  <div class="contact contact--email">
    <svg viewBox="0 0 24 24" aria-hidden="true">
      <circle cx="12" cy="12" r="12" fill="var(--accent)"/>
      <rect x="5.5" y="7.5" width="13" height="9" rx="1" fill="none" stroke="#fff" stroke-width="1.6"/>
      <path d="M5.8 8l6.2 5 6.2-5M5.8 16l4.5-4M18.2 16l-4.5-4" fill="none" stroke="#fff" stroke-width="1.4"/>
    </svg>
    <span>derek@lumbrella-shop.example</span>
  </div>

  <div class="rule"></div>
  <p class="website">www.lumbrella-shop.example</p>
</section>

<section class="card card--back">
  <svg class="wordmark" viewBox="0 0 548 90" aria-label="Lumbrella">
    <text x="274" y="80" text-anchor="middle" font-size="78" textLength="543" lengthAdjust="spacingAndGlyphs">LUMBRELLA</text>
  </svg>
  <p class="website">www.lumbrella-shop.example</p>
</section>

</body>
</html>
```